Website redesign

We need a bold revamp of our website (http://www.brantocksparkworks.co.nz/)
which at the moment looks dated. We want a crisp, fresh and bold look. The background image behind web page can go. Open to complete new layout

Target Market(s)

Electrical contracting company- working in the domestic and commercial field

Coding

Coded - Design and coding required

Number of Pages Required

5+ page

Font styles to use
Sans Serif

Colors

Designer to choose colors to be used in the design.

```html
<!DOCTYPE html>
<html lang="en">
<head>
<meta charset="utf-8">
<title>Brantock Sparkworks</title>
<link rel="stylesheet" href="https://fonts.googleapis.com/css2?family=Lato:wght@400;700;900&display=swap">
<style>
:root{
  --red:#e30b17;
  --ink:#111111;
  --dark:#1d1d1d;
  --text:#333333;
  --grey:#ededed;
  --white:#ffffff;
  --muted:#cfcfcf;
}
*{box-sizing:border-box;margin:0;padding:0}
html,body{width:1200px;height:3169px;overflow:hidden}
body{position:relative;font-family:'Lato',Arial,sans-serif;color:var(--text);background:var(--white)}
.abs{position:absolute}
.topbar{left:0;top:0;width:1200px;height:46px;background:var(--ink);color:var(--white)}
.social{left:76px;top:15px;display:flex;gap:12px}
.social span{width:16px;height:16px;border-radius:50%;background:var(--white);display:block}
.topphone{right:76px;top:14px;font-size:14px;font-weight:700;display:flex;align-items:center;gap:10px}
.header{left:0;top:46px;width:1200px;height:150px;background:var(--white)}
.brand{display:flex;align-items:center;gap:10px}
.brand-mark{width:26px;height:26px;background:var(--red)}
.brand-name{font-size:30px;font-weight:900;color:var(--ink);line-height:1;letter-spacing:-0.5px}
.nav{left:0;width:1200px;font-size:14px;font-weight:700;color:var(--ink)}
.nav a{position:absolute;color:var(--ink);text-decoration:none;transform:translateX(-50%)}
.nav a.active{color:var(--red)}
.hero-stripe{left:0;top:172px;width:1200px;height:30px;background:var(--red);clip-path:polygon(0 80%,100% 0,100% 25%,0 100%)}
.hero{left:0;top:200px;width:1200px;height:529px;background:linear-gradient(100deg,#6d7888 0%,#9aa4b0 35%,#5b5f66 65%,#8e9096 100%)}
.hero-base{left:0;top:697px;width:1200px;height:32px;background:var(--ink);clip-path:polygon(0 0,100% 0,100% 0,0 100%)}
.hero-label{left:76px;top:524px;width:304px;height:68px;background:rgba(17,17,17,.9);color:var(--white);font-size:44px;font-weight:700;letter-spacing:1px;display:flex;align-items:center;padding-left:18px}
.dots{left:74px;top:626px;display:flex;gap:6px}
.dots span{width:11px;height:11px;border-radius:50%;background:var(--ink)}
.dots span.on{background:var(--red)}
.title{left:0;width:1200px;text-align:center;font-size:31px;font-weight:700;color:var(--ink)}
.title em{font-style:normal;color:var(--red)}
.lead{left:40px;width:1120px;text-align:center;font-size:15.5px;line-height:30px;color:var(--text)}
.btn{width:182px;height:50px;left:509px;background:var(--dark);color:var(--white);font-size:14px;font-weight:700;display:flex;align-items:center;justify-content:center;letter-spacing:.3px}
.band-services{left:0;top:1030px;width:1200px;height:640px;background:var(--grey);clip-path:polygon(0 6%,100% 0,100% 94%,0 100%)}
.card{top:1257px;width:241px;height:230px;background:var(--white);text-align:center;padding-top:30px}
.card.active{outline:4px solid var(--red);outline-offset:-4px}
.card h3{font-size:21px;font-weight:700;color:var(--red);margin-top:22px}
.card p{font-size:13.5px;line-height:21px;color:var(--text);margin-top:10px;padding:0 20px}
.card-shadow{top:1488px;width:200px;height:22px;background:radial-gradient(ellipse at center top,rgba(0,0,0,.35),rgba(0,0,0,0) 70%)}
.arrow{top:1356px}
.tile{width:340px;height:241px}
.tile-text{background:#3b3f2c;color:var(--white);text-align:center;padding:48px 10px 0}
.tile-text h4{font-size:21px;font-weight:700;color:#f2e23a;line-height:27px}
.tile-text p{font-size:14px;line-height:27px;margin-top:12px}
.band-partners{left:0;top:2456px;width:1200px;height:250px;background:var(--grey);clip-path:polygon(0 0,100% 11%,100% 92%,0 100%)}
.partners-title{left:0;top:2525px;width:1200px;text-align:center;font-size:14px;font-weight:700;color:var(--ink);letter-spacing:.3px}
.badge{top:2572px;height:62px;background:#d9d9d9}
.footer{left:0;top:2664px;width:1200px;height:440px;background:var(--dark);clip-path:polygon(0 9.5%,100% 0,100% 100%,0 100%)}
.fcol{top:2744px;color:var(--white)}
.fcol h5{font-size:16px;font-weight:700;letter-spacing:.2px;margin-bottom:12px}
.fcol li{list-style:none;font-size:13.5px;line-height:33.3px;color:var(--muted)}
.contact li{display:flex;align-items:center;gap:16px}
.bottombar{left:0;top:3102px;width:1200px;height:67px;background:var(--ink);color:var(--muted)}
.copyright{left:76px;top:28px;font-size:11.5px}
.social-foot{right:110px;top:24px;display:flex;gap:16px}
.social-foot span{width:18px;height:18px;border-radius:50%;background:var(--white);display:block}
</style>
</head>
<body>

<div class="abs topbar">
  <div class="abs social"><span></span><span></span><span></span><span></span><span></span></div>
  <div class="abs topphone">
    <svg width="13" height="13" viewBox="0 0 24 24"><path fill="#fff" d="M6.6 10.8a15 15 0 0 0 6.6 6.6l2.2-2.2c.3-.3.7-.4 1-.2 1.1.4 2.3.6 3.6.6.6 0 1 .4 1 1V20c0 .6-.4 1-1 1A17 17 0 0 1 3 4c0-.6.4-1 1-1h3.5c.6 0 1 .4 1 1 0 1.3.2 2.5.6 3.6.1.3 0 .7-.2 1z"/></svg>
    0800 47 31 62 or &nbsp;(06) 555 0172
  </div>
</div>

<header class="abs header">
  <div class="abs brand" style="left:76px;top:26px">
    <span class="brand-mark"></span>
    <span class="brand-name">Brantock Sparkworks</span>
  </div>
  <nav class="abs nav" style="top:58px">
    <a class="active" style="left:585px">HOME</a>
    <a style="left:682px">ABOUT US</a>
    <a style="left:788px">SERVICES</a>
    <a style="left:894px">PROJECTS</a>
    <a style="left:1010px">CONTACT US</a>
    <a style="left:1109px">INFO</a>
  </nav>
</header>

<div class="abs hero" role="img" aria-label="Smiling electrician in a blue hard hat testing wiring in a switchboard"></div>
<div class="abs hero-stripe"></div>
<div class="abs hero-base"></div>
<div class="abs hero-label">ELECTRICAL</div>
<div class="abs dots"><span class="on"></span><span></span><span></span><span></span></div>

<h1 class="abs title" style="top:751px">WELCOME TO <em>BRANTOCK SPARKWORKS</em></h1>
<p class="abs lead" style="top:803px">Brantock Sparkworks is a leading electrical installation and maintenance company based in Wanganui, but servicing all New Zealand.<br>With over 15 professionally qualified and experienced Wanganui electricians, technicians and support staff we are leading the way<br>in providing quality electrical services.</p>
<div class="abs btn" style="top:930px">READ MORE</div>

<div class="abs band-services"></div>
<h2 class="abs title" style="top:1108px">OUR <em>SERVICES</em></h2>
<p class="abs lead" style="top:1162px">Brantock Sparkworks offers all the domestic and commercial electrical services you would expect from an electrical firm, but with dedicated<br>technicans in specialist electrical areas they have the more technical ability and experience than your average sparky.</p>

<svg class="abs arrow" style="left:46px" width="14" height="28" viewBox="0 0 14 28"><path d="M12 2 2 14l10 12" fill="none" stroke="#555" stroke-width="3"/></svg>
<svg class="abs arrow" style="left:1140px" width="14" height="28" viewBox="0 0 14 28"><path d="M2 2l10 12L2 26" fill="none" stroke="#555" stroke-width="3"/></svg>

<div class="abs card active" style="left:76px">
  <svg width="90" height="62" viewBox="0 0 90 62"><rect x="30" y="4" width="30" height="54" rx="6" fill="#111"/><g fill="#fff"><rect x="36" y="12" width="6" height="6"/><rect x="48" y="12" width="6" height="6"/><rect x="36" y="24" width="6" height="6"/><rect x="48" y="24" width="6" height="6"/><rect x="36" y="36" width="6" height="6"/><rect x="48" y="36" width="6" height="6"/></g><path d="M22 16q-6 15 0 30M14 10q-10 21 0 42M68 16q6 15 0 30M76 10q10 21 0 42" fill="none" stroke="#111" stroke-width="4" stroke-linecap="round"/></svg>
  <h3>Alarm Systems</h3>
  <p>Security , Residential,<br>Industrial</p>
</div>
<div class="abs card" style="left:344px">
  <svg width="62" height="62" viewBox="0 0 62 62"><circle cx="31" cy="31" r="26" fill="none" stroke="#111" stroke-width="5"/><path d="M35 10 18 35h12l-4 17 18-27H32z" fill="#111"/></svg>
  <h3>Electrical</h3>
  <p>Commercial &amp; Residential<br>Services</p>
</div>
<div class="abs card" style="left:615px">
  <svg width="80" height="62" viewBox="0 0 80 62"><path d="M10 28 40 6l30 22" fill="none" stroke="#111" stroke-width="5"/><rect x="28" y="26" width="36" height="32" fill="#111"/><circle cx="46" cy="42" r="11" fill="#fff"/><path d="M46 42l-3-7M46 42l7-1M46 42l-4 6" stroke="#111" stroke-width="3"/><path d="M4 36h18M8 44h14M4 52h18" stroke="#111" stroke-width="4"/></svg>
  <h3>Heat Pumps</h3>
  <p>Sales, Installation,<br>Servicing</p>
</div>
<div class="abs card" style="left:883px">
  <svg width="62" height="62" viewBox="0 0 62 62"><path d="M16 30a10 10 0 0 1 4-19 14 14 0 0 1 26 3 9 9 0 0 1 0 16z" fill="#111"/><rect x="20" y="22" width="22" height="38" rx="4" fill="#111" stroke="#fff" stroke-width="3"/><rect x="25" y="29" width="12" height="20" fill="#fff"/><circle cx="31" cy="54" r="2" fill="#fff"/></svg>
  <h3>Phone Data</h3>
  <p>NetWork Cabling</p>
</div>
<div class="abs card-shadow" style="left:96px"></div>
<div class="abs card-shadow" style="left:364px"></div>
<div class="abs card-shadow" style="left:635px"></div>
<div class="abs card-shadow" style="left:903px"></div>

<div class="abs btn" style="top:1538px">VIEW ALL SERVICES</div>

<h2 class="abs title" style="top:1704px">OUR <em>PROJECTS</em></h2>
<p class="abs lead" style="top:1758px">Here are just a few of our more recent major projects Brantock Sparkworks has completed.</p>

<div class="abs tile" style="left:76px;top:1813px;background:linear-gradient(180deg,#b9d3ea 0%,#c8323a 30%,#2f4f86 45%,#6b6a66 100%)" role="img" aria-label="Clothing shop front with red and blue signage"></div>
<div class="abs tile tile-text" style="left:431px;top:1813px">
  <h4>Rata Retirement Home -<br>New build</h4>
  <p>Rata Hillcrest Retirement Village -<br>Everything electrical including TV, power,<br>heat pumps and phones to 25 houses.</p>
</div>
<div class="abs tile" style="left:786px;top:1813px;background:linear-gradient(180deg,#4f6b4c 0%,#e4e4e4 35%,#c9cbcd 60%,#6c6f73 100%)" role="img" aria-label="Car dealership showroom with cars parked in front"></div>
<div class="abs tile" style="left:76px;top:2071px;background:linear-gradient(180deg,#dfe6ee 0%,#c9c3b7 30%,#8a3a34 50%,#7a7a78 100%)" role="img" aria-label="Corner retail building on a town street"></div>
<div class="abs tile" style="left:431px;top:2071px;background:linear-gradient(180deg,#7fb2e3 0%,#b3473c 35%,#c9cacb 75%,#5e6064 100%)" role="img" aria-label="Red brick heritage commercial building with parked cars"></div>
<div class="abs tile" style="left:786px;top:2071px;background:linear-gradient(180deg,#d8e2ea 0%,#b9c3c9 40%,#6f8aa0 60%,#8d8f8e 100%)" role="img" aria-label="Modern corner shop building with glass frontage"></div>

<div class="abs btn" style="top:2366px">VIEW ALL PROJECTS</div>

<div class="abs band-partners"></div>
<div class="abs partners-title">WE ARE AUTHORISED INSTALLERS FOR</div>
<div class="abs badge" style="left:440px;width:134px"></div>
<div class="abs badge" style="left:610px;width:144px"></div>

<footer class="abs footer"></footer>
<div class="abs fcol" style="left:76px">
  <h5>SITE MAP</h5>
  <ul><li>Home</li><li>About Us</li><li>Services</li><li>Projects</li><li>Contact Us</li><li>Info</li></ul>
</div>
<div class="abs fcol" style="left:323px">
  <h5>SERVICES</h5>
  <ul><li>Alarms</li><li>Appliances</li><li>Electrical</li><li>Fire/Smoke</li><li>Heat Pumps</li><li>IQP Building Compliance</li><li>Phone/Data</li><li>Security</li><li>TV</li></ul>
</div>
<div class="abs fcol" style="left:611px">
  <h5>QUICK LINKS</h5>
  <ul><li>Residential Electrical</li><li>Commercial Electrical</li><li>Kowhai Heat Pumps</li><li>Fire Alarms</li><li>Security Cameras</li><li>Hot Water Cylinders</li><li>CCTV Cameras</li></ul>
</div>
<div class="abs fcol contact" style="left:871px">
  <h5>CONTACT INFO</h5>
  <ul>
    <li><svg width="12" height="14" viewBox="0 0 24 28"><path d="M12 0a10 10 0 0 0-10 10c0 8 10 18 10 18s10-10 10-18A10 10 0 0 0 12 0zm0 14a4 4 0 1 1 0-8 4 4 0 0 1 0 8z" fill="#fff"/></svg>14 Korimako Lane, Wanganui 4500</li>
    <li><svg width="12" height="12" viewBox="0 0 24 24"><path fill="#fff" d="M6.6 10.8a15 15 0 0 0 6.6 6.6l2.2-2.2c.3-.3.7-.4 1-.2 1.1.4 2.3.6 3.6.6.6 0 1 .4 1 1V20c0 .6-.4 1-1 1A17 17 0 0 1 3 4c0-.6.4-1 1-1h3.5c.6 0 1 .4 1 1 0 1.3.2 2.5.6 3.6.1.3 0 .7-.2 1z"/></svg>0800 47 31 62 &nbsp;or &nbsp;(06) 555 0172</li>
    <li><svg width="13" height="12" viewBox="0 0 26 24"><rect x="6" y="0" width="14" height="6" fill="#fff"/><rect x="0" y="8" width="26" height="10" fill="#fff"/><rect x="6" y="15" width="14" height="9" fill="#fff" stroke="#1d1d1d" stroke-width="2"/></svg>(06) 555 0184</li>
    <li><svg width="13" height="10" viewBox="0 0 26 20"><rect width="26" height="20" fill="#fff"/><path d="M0 0l13 11L26 0" fill="none" stroke="#1d1d1d" stroke-width="2"/></svg>office@brantockspark.co.nz</li>
  </ul>
</div>

<div class="abs bottombar">
  <div class="abs copyright">Copyright © 2018 Brantock Sparkworks &nbsp;All Right Reserved</div>
  <div class="abs social-foot"><span></span><span></span><span></span><span></span><span></span></div>
</div>

</body>
</html>
```